Wine Label Design

A wine label for 750ml bottles. Same label for different varieties with the variety / region / vintage to be updated as required.
Brand: Beyond the Ridge
Product Use: Front and Back label suitable for a 750 ml bottle (preferably Burgundy bottles)
Design Brief: Beyond the Ridge is a small winery that produces limited amounts of hand crafted wines that are aimed at the mid to top end of the market and requires a label befitting the work that goes into the creation of the wine. In terms of style i don't have any preconceptions and am open to a broad range of design suggestions at the same level of existing premium brands or innovative brands.
Must Have for Front label
Front Label
Beyond the Ridge
2013
Grampians
Shiraz
750ML (should be in smaller text)
Alc. 14% by Vol. (should be in smaller text)
Must Have for Back Label
Beyond the Ridge
2013
Grampians
Shiraz
www.beyondtheridge.com.au (should be in smaller text)
Product of Australia
Alc.14% by Vol. (should be in smaller text)
Contains preservative 220(should be in smaller text)
Below are some guides for dimensions:
The Front Label Size can be between
100 - 120 mm (Width) x 70 - 85 mm (Height)
The back label size can be between
90 mm (Width) x 70 - 85 mm (Height)
Target Market(s)
Medium to top end of the wine market who require the label to be a reflection of the wine.
Industry/Entity Type
Product
Colors
Designer to choose colors to be used in the design.
Look and feel

```html
<!DOCTYPE html>
<html lang="en">
<head>
<meta charset="utf-8">
<title>Beyond the Ridge – Grampians Shiraz Label</title>
<link rel="stylesheet" href="https://fonts.googleapis.com/css2?family=Raleway:wght@300&family=Playfair+Display:wght@400&family=Courier+Prime&display=swap">
<style>
  :root {
    --backdrop: #ece7de;
    --label: #ffffff;
    --ink-grey: #5d5d5d;
    --ink-dark: #2f2f2f;
    --wine-red: #b5192d;
    --vineyard-red: #c85a6a;
    --vineyard-sun: #efe3bd;
  }
  * { margin: 0; padding: 0; box-sizing: border-box; }
  html, body {
    width: 1200px;
    height: 900px;
    overflow: hidden;
    background: var(--backdrop);
  }
  .canvas {
    position: relative;
    width: 1200px;
    height: 900px;
  }
  .front-label {
    position: absolute;
    left: 322px;
    top: 143px;
    width: 556px;
    height: 614px;
    background: var(--label);
    box-shadow: 0 2px 10px rgba(0, 0, 0, 0.08);
  }
  .brand-name {
    position: absolute;
    top: 78px;
    left: 0;
    width: 100%;
    text-align: center;
    font-family: "Raleway", sans-serif;
    font-weight: 300;
    font-size: 24px;
    letter-spacing: 4px;
    color: var(--ink-grey);
  }
  .vineyard-scene {
    position: absolute;
    top: 155px;
    left: 173px;
    width: 210px;
    height: 150px;
    border-radius: 40% 45% 20% 20%;
    background: linear-gradient(180deg, var(--vineyard-sun) 0%, #f3e7e8 35%, var(--vineyard-red) 70%, #e9e4e4 100%);
    opacity: 0.85;
  }
  .wine-title {
    position: absolute;
    top: 362px;
    left: 0;
    width: 100%;
    display: flex;
    justify-content: center;
    font-weight: 400;
  }
  .wine-title-inner {
    display: flex;
    flex-direction: column;
    align-items: flex-end;
  }
  .region {
    font-family: "Raleway", sans-serif;
    font-weight: 300;
    font-size: 13px;
    letter-spacing: 3px;
    color: var(--ink-grey);
    line-height: 14px;
    margin-right: 82px;
  }
  .variety-vintage {
    font-family: "Playfair Display", serif;
    font-weight: 400;
    font-size: 62px;
    line-height: 66px;
    white-space: nowrap;
  }
  .variety { color: var(--wine-red); }
  .vintage { color: var(--ink-grey); margin-left: 14px; }
  .bottle-details {
    position: absolute;
    top: 527px;
    left: 0;
    width: 100%;
    text-align: center;
    font-family: "Courier Prime", monospace;
    color: var(--ink-dark);
    font-size: 19px;
    line-height: 27px;
  }
  .bottle-details small { font-size: 15px; }
</style>
</head>
<body>
  <main class="canvas">
    <section class="front-label">
      <p class="brand-name">BEYOND THE RIDGE</p>
      <div class="vineyard-scene" role="img" aria-label="Sketched vineyard landscape with red vine rows, cypress trees and a farmhouse on rolling hills"></div>
      <h1 class="wine-title">
        <span class="wine-title-inner">
          <span class="region">GRAMPIANS</span>
          <span class="variety-vintage"><span class="variety">Shiraz</span><span class="vintage">2013</span></span>
        </span>
      </h1>
      <p class="bottle-details">
        <small>Alc.</small> 750ml<br>
        14% <small>by</small> Vol.
      </p>
    </section>
  </main>
</body>
</html>
```